New Property management company business cards

Looking for a new business card, to reflect new younger ownership
Card should be clean, simple and professional but with a modern layout that is conveys our new logo and business model

Key aspects of the business:

Property Management
Facility Maintenance
Project Management
Tenant Improvements

Mailing Address:
PO BOX 7816
Ridgefield CA, 95412

Phone: 209-418-6071
Direct: 209-418-6074

Doyle Marsh
President

Target Market(s)

Commercial property owners

Industry/Entity Type

Real Estate property management

Contact Information for Business Card

Open to all designs but lean toward vertical layouts

Requirements
Must have
• Logo and space to customize name and contact info

```html
<!DOCTYPE html>
<html lang="en">
<head>
<meta charset="utf-8">
<title>Valmont Property Management – Business Card</title>
<link rel="stylesheet" href="https://fonts.googleapis.com/css2?family=Arimo:wght@400;700&display=swap">
<style>
  :root {
    --bg: #e4e4e4;
    --paper: #ffffff;
    --charcoal: #333333;
    --ink: #2e2f3a;
    --grey: #5a5a5a;
    --rule: #9a9a9a;
    --teal: #1aa3a3;
    --white: #f4f4f4;
  }
  * { box-sizing: border-box; margin: 0; padding: 0; }
  html, body { width: 1200px; height: 802px; overflow: hidden; }
  body {
    background: var(--bg);
    font-family: "Arimo", Arial, sans-serif;
    display: flex;
    align-items: center;
    justify-content: center;
    gap: 40px;
  }
  .card {
    width: 540px;
    height: 309px;
    position: relative;
    box-shadow: 0 2px 6px rgba(0,0,0,.12);
  }
  /* Front */
  .card--front { background: var(--paper); display: flex; align-items: center; }
  .brand {
    width: 250px;
    padding-left: 40px;
    color: var(--ink);
    font-weight: 700;
  }
  .brand__name { font-size: 30px; letter-spacing: 4px; line-height: 1; }
  .brand__tag { font-size: 10px; letter-spacing: 3.6px; margin-top: 6px; }
  .divider { width: 1px; height: 150px; background: var(--rule); }
  .contact { padding-left: 26px; color: var(--grey); font-size: 14px; line-height: 1.3; }
  .contact__name { color: var(--teal); font-weight: 700; font-size: 21px; letter-spacing: .5px; }
  .contact__title { margin-bottom: 12px; font-size: 15px; }
  .contact__row { display: flex; align-items: center; gap: 8px; }
  .contact__row svg { width: 13px; height: 13px; flex: none; }
  .contact__address { margin-top: 14px; }
  /* Back */
  .card--back { background: var(--charcoal); color: var(--white); }
  .card--back .brand {
    position: absolute; right: 36px; top: 48px;
    width: auto; padding: 0; color: var(--white); text-align: right;
  }
  .card--back .brand__name { font-size: 38px; letter-spacing: 5px; }
  .card--back .brand__tag { font-size: 11px; letter-spacing: 5px; }
  .services {
    position: absolute; right: 36px; top: 168px;
    text-align: right; font-size: 14px; line-height: 1.55;
  }
  .services__heading { color: var(--teal); font-weight: 700; font-size: 17px; margin-bottom: 2px; padding-right: 13px; }
  .services__list { list-style: none; }
  .services__list li::after {
    content: ""; display: inline-block; width: 5px; height: 5px;
    background: var(--teal); border-radius: 50%;
    margin-left: 8px; vertical-align: middle;
  }
</style>
</head>
<body>
  <section class="card card--front" aria-label="Business card front">
    <div class="brand">
      <div class="brand__name">VALMONT</div>
      <div class="brand__tag">PROPERTY MANAGEMENT</div>
    </div>
    <div class="divider"></div>
    <div class="contact">
      <div class="contact__name">DOYLE MARSH</div>
      <div class="contact__title">President</div>
      <div class="contact__row">
        <svg viewBox="0 0 16 16" aria-hidden="true"><path fill="#1aa3a3" d="M4 1l3 3-2 2c1 2 3 4 5 5l2-2 3 3-2 3C7 15 1 9 1 3z"/></svg>
        <span>209-418-6071</span>
      </div>
      <div class="contact__row">
        <svg viewBox="0 0 16 16" aria-hidden="true"><rect x="4" y="1" width="8" height="14" rx="1.5" fill="none" stroke="#1aa3a3" stroke-width="1.6"/><circle cx="8" cy="12.5" r="1" fill="#1aa3a3"/></svg>
        <span>209-418-6074</span>
      </div>
      <div class="contact__address">PO BOX 7816<br>Ridgefield CA, 95412</div>
    </div>
  </section>

  <section class="card card--back" aria-label="Business card back">
    <div class="brand">
      <div class="brand__name">VALMONT</div>
      <div class="brand__tag">PROPERTY MANAGEMENT</div>
    </div>
    <div class="services">
      <div class="services__heading">OUR SERVICES</div>
      <ul class="services__list">
        <li>Property Management</li>
        <li>Facility Maintenance</li>
        <li>Project Management</li>
        <li>Tenant Improvements</li>
      </ul>
    </div>
  </section>
</body>
</html>
```